Visitenkarten-Design für Osteopathie-Praxis
Zielgruppe
Es handelt sich um eine Osteopathie-Praxis mit einer eher gehobenen (preislich) Zielgruppe mit allen Altersklassen. Die Praxis soll im leichten skandinavischen Stil eingerichtet werden und die Internetseite mit folgenden Theme entworfen werden: http://demo.pixelhaus-vorlagen.de/#pv_merle
Aufgabenstellung
Das Design muss leicht und klar sein. Es darf nicht überlastet sein. Auf die Vorderseite soll das Logo kommen und auf die Rückseite die Kontaktdaten sowie die Leistungen (Osteopath D.O., Physiotherapeut, Heilpraktiker) und meinen Name. Ich habe Beispiele zugefügt. Das Logo besteht nur aus dem Kreis. Als Text soll 'Vitalis - Osteopathische Medizin' zum Logo kommen dabei sollte einen Font genutzt werden den ich auf der Internetseite wieder nutzen kann.

```html
<!DOCTYPE html>
<html lang="de">
<head>
<meta charset="utf-8">
<title>Vitalis – Visitenkarte</title>
<link rel="stylesheet" href="https://fonts.googleapis.com/css2?family=Fira+Sans:wght@300;400;500;600&display=swap">
<style>
  :root {
    --teal: #62c6b8;
    --teal-light: #77cec3;
    --teal-deep: #5bc3b4;
    --paper: #ffffff;
    --backdrop: #ededed;
    --ink: #2b2b2b;
    --ink-soft: #3c3c3c;
  }
  * { margin: 0; padding: 0; box-sizing: border-box; }
  html, body {
    width: 1200px; height: 1200px; overflow: hidden;
    background: var(--backdrop);
    font-family: "Fira Sans", Arial, sans-serif;
  }
  .stage { position: relative; width: 1200px; height: 1200px; }

  .card {
    position: absolute;
    width: 548px; height: 355px;
    overflow: hidden;
  }

  /* Front side */
  .card-front {
    left: 492px; top: 220px;
    background: linear-gradient(180deg, var(--teal-light) 0%, var(--teal-deep) 100%);
    color: var(--paper);
  }
  .brand-name {
    position: absolute; left: 26px; top: 28px;
    font-size: 39px; font-weight: 500; letter-spacing: 0.2px; line-height: 1;
  }
  .brand-tagline {
    position: absolute; left: 27px; top: 78px;
    font-size: 17px; font-weight: 500; line-height: 1;
  }

  /* Back side */
  .card-back {
    left: 198px; top: 623px;
    background: var(--paper);
    color: var(--ink);
  }
  .logo-mark {
    position: absolute; right: 28px; top: 19px;
    display: flex; align-items: center; gap: 10px;
  }
  .logo-mark .mark-circle {
    width: 74px; height: 74px; border-radius: 50%;
    background: var(--teal);
  }
  .logo-mark .mark-name {
    order: -1;
    font-size: 18px; font-weight: 500; color: var(--teal);
  }
  .person-name {
    position: absolute; left: 30px; top: 112px;
    font-size: 27px; font-weight: 600; color: var(--teal); line-height: 1;
  }
  .person-services {
    position: absolute; left: 31px; top: 143px;
    font-size: 13px; font-weight: 400; color: var(--ink-soft); line-height: 1;
  }
  .address {
    position: absolute; left: 31px; top: 178px;
    font-size: 19px; font-weight: 300; line-height: 27px;
  }
  .contact {
    position: absolute; left: 31px; top: 240px;
    font-size: 19px; font-weight: 300; line-height: 27px;
    display: grid; grid-template-columns: 80px auto;
  }
  .website {
    position: absolute; left: 31px; top: 303px;
    font-size: 19px; font-weight: 300; line-height: 27px;
  }
  .base-band {
    position: absolute; left: 0; bottom: 0;
    width: 100%; height: 12px;
    background: var(--teal);
  }
</style>
</head>
<body>
<main class="stage">
  <section class="card card-front" aria-label="Vorderseite">
    <div class="brand-name">Vitalis</div>
    <div class="brand-tagline">Osteopathische Medizin</div>
  </section>

  <section class="card card-back" aria-label="Rückseite">
    <div class="logo-mark">
      <span class="mark-circle"></span>
      <span class="mark-name">Vitalis</span>
    </div>
    <h1 class="person-name">Julien Marchetti</h1>
    <p class="person-services">Osteopath D.O. · Physiotherapeut · Heilpraktiker</p>
    <address class="address" style="font-style:normal">
      Lindenhofweg 7<br>
      72336 Balingen
    </address>
    <div class="contact">
      <span>Tel.:</span><span>0711 / 4820 17 39</span>
      <span>E-Mail:</span><span>info@vitalis-osteo.de</span>
    </div>
    <div class="website">www.vitalis-osteo.de</div>
    <div class="base-band"></div>
  </section>
</main>
</body>
</html>
```